FItness Bootcamp Flyer

We need an A4 flyer to distribute on an advertising board, and also distribute in the mail.

It should contain a photo(s) of females exercising and having fun outdoors.

It should contain the following text and if you think it could be worded better please change as I'm just looking at getting people to come along:

- KestrelMove Studio Outdoor Bootcamp
Get moving, get fit and feel great

Commencing 19th May

Get results before the winter season
6 Week Bootcamp for $49. Limited numbers!
Or casual visit $10 per session

Now is the time to:
- Lose Weight and Tone-up
- Build Strength and Endurance
- Increase Cardio Fitness
- Improve Your Energy and Vitality
- Fun Varied and Exciting Training Programs
- ALL Fitness Levels

LADIES ONLY BOOTCAMP SUBIACO
Monday 6:30-7:15am, 8:30-9:15am
Wednesday 6:30-7:!5am, 8:30-9:15am
Friday 8:30-9:15am,

Register you place now on 0428 574 812 or email: kestrelmovestudio@fernmail.net

chirpline.com/KestrelMove Studio

Target Market(s)

Females 20-60yrs

Industry/Entity Type

Advertising

Requirements
Nice to have
• - We like the words and style of the Harbourline Open Air Training flyer attached
- Also the Vanta Group brochure
- I like the colour Blue, Green, Pink. They don't all have to be used but at least one would be nice thank you

```html
<!DOCTYPE html>
<html lang="en">
<head>
<meta charset="utf-8">
<title>KestrelMove Studio Outdoor Bootcamp Flyer</title>
<link rel="stylesheet" href="https://fonts.googleapis.com/css2?family=PT+Sans:wght@400;700&display=swap">
<style>
  :root {
    --page: #f2f2f2;
    --sky-deep: #173a93;
    --sky-mid: #3f76c8;
    --sky-light: #8fb6e0;
    --lake: #5f9a86;
    --grass: #2fb33a;
    --grass-deep: #1f9a2c;
    --brand-blue: #1d4fa3;
    --accent-orange: #f0861d;
    --white: #ffffff;
    --ink: #111111;
    --panel: rgba(70, 170, 100, 0.55);
  }
  * { margin: 0; padding: 0; box-sizing: border-box; }
  html, body {
    width: 1200px; height: 1200px; overflow: hidden;
    background: var(--page);
    font-family: "PT Sans", Arial, sans-serif;
  }
  .flyer {
    position: absolute; left: 175px; top: 0;
    width: 849px; height: 1200px; overflow: hidden;
  }
  .scenery {
    position: absolute; inset: 0;
    background: linear-gradient(to bottom,
      var(--sky-deep) 0%, var(--sky-mid) 18%, var(--sky-light) 32%,
      #7fa9a4 40%, var(--lake) 50%, #4aa55a 62%,
      var(--grass) 75%, var(--grass-deep) 100%);
  }
  .sun-glow {
    position: absolute; left: 420px; top: 40px; width: 260px; height: 260px;
    border-radius: 50%;
    background: radial-gradient(circle, rgba(255,255,255,0.95) 0%, rgba(255,255,255,0.35) 25%, rgba(255,255,255,0) 65%);
  }
  .athlete-photo {
    position: absolute; left: 20px; top: 20px; width: 165px; height: 805px;
    border-radius: 70px 70px 30px 30px;
    background: linear-gradient(to bottom, #3a2e2a 0%, #222 35%, #1a1a1a 100%);
    opacity: 0.85;
  }
  .line { position: absolute; white-space: nowrap; }
  .center { left: 0; right: 0; text-align: center; }
  .brand-top {
    top: 42px; left: 180px; width: 700px; text-align: center;
    font-size: 30px; line-height: 30px; font-weight: 700; color: var(--white);
  }
  .tagline {
    top: 85px; left: 180px; width: 700px; text-align: center;
    font-size: 22px; line-height: 22px; color: var(--ink);
  }
  .start-date {
    top: 170px; left: 180px; width: 700px; text-align: center;
    font-size: 38px; line-height: 38px; color: var(--ink);
  }
  .offer {
    position: absolute; top: 233px; left: 180px; width: 700px; text-align: center;
    font-size: 19px; line-height: 28px; color: var(--ink);
  }
  .benefits {
    position: absolute; left: 458px; top: 370px; width: 370px; height: 249px;
    background: var(--panel); border-radius: 16px;
    padding: 14px 12px; font-size: 19px; line-height: 27px; color: var(--white);
  }
  .benefits h2 { font-size: 19px; font-weight: 400; color: var(--accent-orange); }
  .benefits ul { list-style: none; }
  .schedule {
    position: absolute; left: 209px; top: 700px;
    font-size: 19px; line-height: 28px; color: var(--ink);
  }
  .brand-bottom {
    top: 868px; font-size: 38px; line-height: 38px; font-weight: 700; color: var(--brand-blue);
  }
  .cta { font-weight: 700; color: var(--ink); font-size: 32px; line-height: 32px; }
  .cta-register { top: 962px; }
  .cta-phone { top: 1018px; }
  .cta-email { top: 1072px; }
  .cta-social { top: 1126px; }
</style>
</head>
<body>
  <main class="flyer">
    <div class="scenery" role="img" aria-label="Mountain lake landscape under a bright sunny blue sky, fading to green"></div>
    <div class="sun-glow"></div>
    <div class="athlete-photo" role="img" aria-label="Woman in black workout clothes doing a high-knee exercise"></div>

    <h1 class="line brand-top">KestrelMove Studio Outdoor Bootcamp</h1>
    <p class="line tagline">Get moving, get fit and feel great</p>
    <p class="line start-date">Commencing 19th May</p>
    <p class="offer">Get results before the winter season<br>6 Week Bootcamp for $49. Limited numbers!<br>Or casual visit $10 per session</p>

    <section class="benefits">
      <h2>Now is the time to:</h2>
      <ul>
        <li>- Lose Weight and Tone-up</li>
        <li>- Build Strength and Endurance</li>
        <li>- Increase Cardio Fitness</li>
        <li>- Improve Your Energy and Vitality</li>
        <li>- Fun Varied and Exciting Training Programs</li>
        <li>- ALL Fitness Levels</li>
      </ul>
    </section>

    <p class="schedule">LADIES ONLY BOOTCAMP SUBIACO<br>Monday 6:30-7:15am, 8:30-9:15am<br>Wednesday 6:30-7:15am, 8:30-9:15am<br>Friday 8:30-9:15am,</p>

    <p class="line center brand-bottom">KestrelMove Studio Outdoor Bootcamp</p>
    <p class="line center cta cta-register">REGISTER YOU PLACE NOW</p>
    <p class="line center cta cta-phone">0428 574 812</p>
    <p class="line center cta cta-email">kestrelmovestudio@fernmail.net</p>
    <p class="line center cta cta-social">chirpline.com/KestrelMove Studio</p>
  </main>
</body>
</html>
```